Flyer-Design für Werbeflyer Teamentwicklung/Coaching als pdf
Zielgruppe
ich berate Personen, Teams und Organisationseinheiten, überwiegend im Profitbereich. (Internationale Konzerne). Mein Beratungsspektrum ist Führung, Prozessverbesserungen, Teamentwicklung
Aufgabenstellung
Der Text ist in Anlehnung an meine HP, Teamentwicklung und Coaching und es sollte eine übersichtliche, infomative 1-2 Seiten entstehen, die ich als erste Werbung/Kontaktaufnahme versenden kann. Die Seiten sollen klar einen Überblick über mein "Schaffen" geben, sollen aber auch schon etwas von meiner Arbeitsweise deutlich machen. (Ich begriefe schnell, formuliere klar und arbeite sehr zielorientiert - allerdings auch schnörkellos!) Diese Seiten sollten überwiegend als Anhang an eine Mail fungieren, im Ausnahmefall aber auch versendet werden.
Das Logo, die Farbe, etc. analog zu meiner HP - ich lass mich da aber auch gern beraten, falls sie andere Ideen haben

```html
<!DOCTYPE html>
<html lang="de">
<head>
<meta charset="utf-8">
<title>Teamentwicklung – Brigitte Moser</title>
<link rel="stylesheet" href="https://fonts.googleapis.com/css2?family=Open+Sans:wght@400;600&family=Tinos:wght@700&display=swap">
<style>
  :root{
    --sage:#b9c6c1;
    --sage-dark:#8f9c98;
    --plum:#7a1150;
    --ink:#6a6e6d;
    --text:#5e6261;
    --white:#ffffff;
  }
  *{margin:0;padding:0;box-sizing:border-box}
  html,body{width:1200px;height:846px;overflow:hidden;background:var(--white)}
  .flyer{position:relative;width:1200px;height:846px;overflow:hidden;background:var(--white);font-family:"Open Sans",Arial,sans-serif}
  .hero-photo{position:absolute;left:0;top:0;width:746px;height:846px;
    background:linear-gradient(180deg,#2f86c4 0%,#6cc0dc 18%,#a9dde6 30%,#4fc0c4 35%,#7fcfcb 46%,#c9d9cf 52%,#b8a58c 62%,#8c7a66 80%,#6e6052 100%)}
  .accent-bar{position:absolute;left:1043px;top:0;width:109px;height:228px;background:var(--plum)}
  .top-band{position:absolute;left:0;top:27px;width:1200px;height:114px;background:var(--sage)}
  .brand{position:absolute;left:45px;top:27px;width:122px;height:114px;display:flex;align-items:center;justify-content:center;gap:6px;
    background:linear-gradient(90deg,var(--sage-dark) 50%,var(--white) 50%)}
  .brand-square{width:10px;height:10px;background:var(--plum)}
  .brand-name{font-size:15px;font-weight:600;color:var(--ink);background:var(--white);padding:2px 4px;letter-spacing:.5px}
  .quote{position:absolute;left:707px;top:34px;width:464px;height:100px}
  .quote svg{position:absolute;inset:0}
  .quote-text{position:absolute;font-family:"Tinos","Times New Roman",serif;font-weight:700;font-size:20px;color:var(--white);white-space:nowrap}
  .quote-line1{left:30px;top:20px}
  .quote-line2{left:100px;top:54px}
  .quote-mark{position:absolute;font-family:"Tinos",serif;font-weight:700;font-size:34px;color:var(--white);line-height:1}
  .mark-open{left:-10px;top:14px}
  .mark-close{left:444px;top:66px}
  .title{position:absolute;right:48px;top:256px;text-align:right;color:var(--ink);font-weight:600;line-height:1}
  .title-main{font-size:37px;letter-spacing:.5px}
  .title-name{font-size:29px;margin-top:5px;letter-spacing:.5px}
  .title-name span{color:var(--plum)}
  .services{position:absolute;left:820px;top:370px;width:360px;color:var(--text)}
  .services h2{font-size:19px;font-weight:600;letter-spacing:.5px;margin-bottom:16px}
  .services ul{list-style:none}
  .services li{position:relative;padding-left:26px;font-size:19px;line-height:25px;margin-bottom:13px;white-space:nowrap}
  .services li::before{content:"";position:absolute;left:4px;top:8px;width:11px;height:11px;background:var(--plum)}
  .intro{position:absolute;left:302px;top:492px;width:393px;height:311px;background:rgba(255,255,255,.82);border:5px solid rgba(150,150,150,.75);padding:18px 10px 0 20px}
  .intro h1{font-size:32px;line-height:44px;font-weight:400;color:var(--plum);letter-spacing:.3px;margin-bottom:15px}
  .intro p{font-size:17.5px;line-height:25.5px;color:var(--text);white-space:nowrap}
</style>
</head>
<body>
<div class="flyer">
  <div class="hero-photo" role="img" aria-label="Foto: weißer Holzsteg mit Geländer, der über türkisfarbenes Meer unter blauem Himmel führt"></div>
  <div class="accent-bar"></div>
  <div class="top-band"></div>
  <div class="brand"><span class="brand-square"></span><span class="brand-name">Moser</span></div>

  <div class="quote">
    <svg width="464" height="100" viewBox="0 0 464 100" fill="none" stroke="#fff" stroke-width="4">
      <polyline points="60,2 2,2 2,100"/>
      <polyline points="404,2 462,2 462,72"/>
      <polyline points="85,98 2,98"/>
    </svg>
    <span class="quote-mark mark-open">“</span>
    <span class="quote-text quote-line1">Zu erkennen was geschieht,</span>
    <span class="quote-text quote-line2">ist der Beginn der Veränderung.</span>
    <span class="quote-mark mark-close">”</span>
  </div>

  <div class="title">
    <div class="title-main">TEAMENTWICKLUNG</div>
    <div class="title-name">BRIGITTE <span>MOSER</span></div>
  </div>

  <section class="services">
    <h2>DAZU GEHÖREN</h2>
    <ul>
      <li>Eine sorgfältige Analyse<br>der Situation und Festlegung<br>gewünschter Resultate</li>
      <li>Überzeugende und förderliche<br>Methoden, die die Lösungs<br>kompetenzen der Menschen<br>im Team unterstützen</li>
      <li>Klare Führung durch den<br>Widerstreit von Teaminteres-<br>sen zwischen Verändern, Be-<br>wahren, Harmonie und Kon-<br>fliktbearbeitung, klarem Feed-<br>back und Eintracht im Team</li>
      <li>Tragfähigkeit der Ergebnisse</li>
    </ul>
  </section>

  <section class="intro">
    <h1>TEAMENTWICKLUNG</h1>
    <p>Teams sind lebendige Gebilde, die<br>um erfolgreich zu sein, sich immer<br>wieder neu ausrichten und koordi-<br>nieren müssen. Das tun sie in aller<br>Regel ohne fremde Hilfe - aber ab<br>und zu ist es hilfreich, Impulse oder<br>Entwicklungsförderung von außen<br>bekommen.</p>
  </section>
</div>
</body>
</html>
```